Create a Graphic About YOURSELF and PixelHarbor

PixelHarbor would like you (designers) to create an awesome graphic to promote YOURSELF and your profile on PixelHarbor!

Your graphic should communicate your name, your services and should mention PixelHarbor.

The design should be perfect for sharing on Chatterly. Here's an example of what we'd like http://blog.pixelharbor-example.ca/article/333/pixelharbor-launches-3000-hire-me-social-design-contest

Once you submitted your design, we'd love you to share the design ('advertisement') and promote yourself and PixelHarbor to your friends and potential customers. So make your submissions great and get your friends to vote for your design by 'Liking' it on Chatterly!

Prizes:
$1500 - "PixelHarbor Community" prize awarded to the designer with the most Chatterly 'Likes'
5 x $50 for the next 5 'most liked' designs on Chatterly

$1000 - "Hire Me" prize awarded to the designer who receives the most client invites
5 x $50 for the next 5 'most invited' designers

In summary, this is a great opportunity for you to increase your exposure to PixelHarbor customers and win cash prizes. Show off your design skills and get hired by PixelHarbor customers from around the world!

Target Market(s)

Fans, friends and customers of YOU

Industry/Entity Type

Cash

Requirements
Must have
• 1) Include your PixelHarbor user name on the graphic so customers can find you in the PixelHarbor Designer Directory
2) Include the tagline "Hire Me on PixelHarbor.com!" in your graphic design.
3) Share your design's URL on our Chatterly wall at http://chatterly-example.com/pixelharbor and get your friends to 'like' your design.
Nice to have
• 1) Include a tagline that expresses your design approach/philosophy
2) Artwork dimensions: 403 x 403 px
3) You can submit more than 1 design!
Should not have
• You must own the copyright of any images you use including stock imagery.

```html
<!DOCTYPE html>
<html lang="en">
<head>
<meta charset="utf-8">
<title>lumora — Here I am, Hire me</title>
<link rel="stylesheet" href="https://fonts.googleapis.com/css2?family=Poppins:wght@600&family=Questrial&display=swap">
<style>
  :root {
    --strip: #777777;
    --panel: #3b3b3b;
    --decor-light: #555555;
    --decor-dark: #444444;
    --band: #4e4e4e;
    --accent: #ff6a00;
    --muted: #8c8c8c;
    --headline: #8e8e8e;
    --initial: #b0b0b0;
    --mark: #222222;
  }
  html, body {
    margin: 0;
    padding: 0;
    width: 1200px;
    height: 1200px;
    overflow: hidden;
    background: var(--panel);
  }
  .poster {
    display: block;
    width: 1200px;
    height: 1200px;
  }
  .side-strip { fill: var(--strip); }
  .main-panel { fill: var(--panel); }
  .decor-stop-light { stop-color: var(--decor-light); }
  .decor-stop-dark { stop-color: var(--decor-dark); }
  .tagline-band { fill: var(--band); }
  .username {
    font-family: "Poppins", sans-serif;
    font-weight: 600;
    font-size: 50px;
    fill: var(--accent);
    letter-spacing: 0.5px;
  }
  .tagline {
    font-family: "Questrial", sans-serif;
    font-size: 21px;
    fill: var(--muted);
    letter-spacing: 1px;
  }
  .headline {
    font-family: "Questrial", sans-serif;
    font-size: 70px;
    fill: var(--headline);
  }
  .headline-initial {
    font-family: "Questrial", sans-serif;
    font-size: 86px;
    fill: var(--initial);
  }
  .platform-name {
    font-family: "Questrial", sans-serif;
    font-size: 22px;
    fill: var(--mark);
    letter-spacing: 0.5px;
  }
  .platform-dot { fill: var(--mark); }
</style>
</head>
<body>
<svg class="poster" viewBox="0 0 403 403" xmlns="http://www.w3.org/2000/svg">
  <defs>
    <linearGradient id="decor-fade" x1="0" y1="0" x2="1" y2="1">
      <stop class="decor-stop-light" offset="0"/>
      <stop class="decor-stop-dark" offset="1"/>
    </linearGradient>
  </defs>

  <rect class="side-strip" x="0" y="0" width="403" height="403"/>
  <rect class="main-panel" x="63" y="0" width="340" height="403"/>

  <rect class="personal-mark-area" x="68" y="96" width="335" height="307"
        fill="url(#decor-fade)" role="img"
        aria-label="Large faint personal monogram decoration"/>

  <rect class="tagline-band" x="200" y="64" width="203" height="32"/>
  <text class="username" x="388" y="52" text-anchor="end">lumora</text>
  <text class="tagline" x="392" y="88" text-anchor="end">another brain</text>

  <g class="platform-mark">
    <text class="platform-name" transform="translate(36 150) rotate(-90)">PixelHarbor</text>
    <circle class="platform-dot" cx="29" cy="172" r="7"/>
  </g>

  <g class="headline-block">
    <text class="headline-initial" x="4" y="302">H</text>
    <text class="headline" x="66" y="302">ere I am</text>
    <text class="headline-initial" x="4" y="382">H</text>
    <text class="headline" x="66" y="382">ire</text>
    <text class="headline" x="283" y="382">me</text>
  </g>
</svg>
</body>
</html>
```